"The Summit Hour Radio Program" needs 3 banner ad designs

I am seeking the design and creation of 3 differently-designed ”banner ads.” I want them to look as though there is a relation between designs but I don't want them to look the same.
While compatibility is desired, that desire should not be interpreted as sameness.

I need a series of banner ads to be a supplement and a complement to
"The Summit Hour"'s main banner ad page and accompanying site.
http://www.qorvalnet.org/

I am looking for high quality, creative capturing of banner ads that focus on three topic areas, namely, my:

1. Leadership Coaching Program –
“Growth Pathway Mentoring Method™”

2. Training program – “The Craft of a Steady Captain”

and

3. Speaker Interest & Availability banner ad.

It is desired that each banner, and the banners collectively, complement and fit in with the look and feel of the existing, principal banner and the show’s vision and mission. (in the attachment, I have included a copy of this banner for your information).

The final design should commit experience, competence, depth and reliability.

To provide a bit of context for this request, I have included the show's vision and mission statement as well as a brief description of my perspective on each banner ad.

I will of course, provide the winner all of the information, documents, graphic depictions, etc that I have available (during the handover stage) that will enable them to create quality products.

In addition, each banner ad should be delivered as JPEG files in dimensions 728 pixel wide and 90 pixels high each. The following fonts: Trajan Pro Regular or Thomas Condensed Regular are the desired fonts.

The task summary: Design 3 banner ads as described below:

1. Leadership Coaching Program – Growth Pathway Mentoring Method™
My coaching program has a formal structure that has an existing graphic capturing of leadership coaching that that would/should be incorporated in the ad.

2. Training program – The Craft of a Steady Captain
The skills training program description I have included as noted below; it is a program that can also be licensed for use by customers who would wish to use it in their organization. In addition to the creative thinking of graphics artists, it would probably be useful to view the home page graphic at www.trm8k.com. This image might be useful in enhancing the banner ad graphic.

3. Speaking Interest – Availability
Have been and desire using this banner to communicate my interest in generating value and availability as a speaker.

-Vision-
“The Summit Hour”
Shaping Tomorrow via Steady Guidance
*is a powerfully engaging platform for great conversations about leadership and leadership learning.

-Mission-
Build a community of listeners who are informed and enthusiastically engaged with the host and the show’s goal of improving the quality of leadership wherever listeners are living and leading.

Leadership Coaching Banner Ad* = *Growth Pathway Mentoring Method*

for use in designing the Book Ad – The Craft of a Steady Captain:
Turning Into Someone a Team Trusts Gladly*

Concepts Summary *this information is for the design of the banner ad for
the Skills Training Course. It includes quotes that could be excerpted to
include in the banner ad*

-> Picture of book for Craft of a Steady Captain Training Program – *this is additional information for the use in designing the Training program banner ad

You can find the other attachments useful. Please have a look.
I welcome all your creative and original designs. Remember, these are 3 different-looking banner ads - though related in some way.

Project Deadline Extended Reason: The current designs have not included enough variety and creativity. While I am desirous of compatibility of the ad renditions with the central image, I am not interpreting compatibility with sameness of looking to see the same image in each banner ad. I rather think the image differentiation promotes both interest and distinction between the products of book, leadership coaching, speaking, etc. Same image embedded in each banner ad doesn't provide the variety that I think both distinguishes and draws interest. In this regard, most of the current examples include the same pictorial images across designs and the use of just words vs. images from among those provided, As an example a picture of my book on the book banner ad seems more impactful than merely using the words book on the ad for the book; and the picture of a speaker vs. Speaker Availability.I hope this feedback is helpful . Regards,Wilfred Added Saturday, June 3, 2017

Target Market(s)

Online Radio Listeners Can Visit SoundHarbor.com for examples - Will be broadcast on the Business Network

Industry/Entity Type

Business Consultant

Colors

Designer to choose colors to be used in the design.

Requirements
Should not have
• Anything that doesn't speak to the characteristics noted at the end of the summary provided in the description above

```html
<!DOCTYPE html>
<html lang="en">
<head>
<meta charset="utf-8">
<title>Training Program Banner – The Craft of a Steady Captain</title>
<link rel="stylesheet" href="https://fonts.googleapis.com/css2?family=EB+Garamond:ital,wght@0,400;1,400&display=swap">
<style>
  :root {
    --frame: #2c5573;
    --edge: #6e93b0;
    --field-light: #e4eef5;
    --field-mid: #c4d8e7;
    --ink: #1c3450;
    --rule: #3d6384;
    --book-dark: #3f5f78;
    --book-mid: #7f98ab;
    --book-light: #c9c2b4;
  }
  * { margin: 0; padding: 0; box-sizing: border-box; }
  html, body {
    width: 1200px;
    height: 148px;
    overflow: hidden;
    background: #ffffff;
  }
  .banner {
    position: relative;
    width: 1200px;
    height: 148px;
    border: 4px solid var(--frame);
    background:
      radial-gradient(ellipse 420px 90px at 50% 50%, var(--field-light) 0%, var(--field-mid) 60%, var(--edge) 100%);
    overflow: hidden;
    font-family: "EB Garamond", Georgia, serif;
  }
  .book-left {
    position: absolute;
    left: -20px;
    top: -14px;
    width: 270px;
    height: 190px;
    transform: rotate(-8deg);
    background: linear-gradient(135deg, var(--book-mid) 0%, var(--book-dark) 45%, var(--book-light) 100%);
    box-shadow: 4px 4px 10px rgba(0,0,0,0.35);
  }
  .book-right {
    position: absolute;
    right: -14px;
    top: -10px;
    width: 235px;
    height: 180px;
    transform: rotate(6deg);
    background: linear-gradient(160deg, var(--book-dark) 0%, var(--book-mid) 50%, var(--book-light) 100%);
    box-shadow: -4px 4px 10px rgba(0,0,0,0.35);
  }
  .headline {
    position: absolute;
    left: 270px;
    right: 250px;
    top: 22px;
    text-align: center;
    color: var(--ink);
  }
  .program-type {
    font-size: 38px;
    font-weight: 400;
    letter-spacing: 1px;
    line-height: 1;
  }
  .program-rule {
    display: block;
    margin: 10px auto 8px;
    width: 530px;
    height: 2px;
    background: linear-gradient(90deg, transparent 0%, var(--rule) 20%, var(--rule) 80%, transparent 100%);
  }
  .program-title {
    font-size: 33px;
    font-style: italic;
    line-height: 1;
    letter-spacing: 0.5px;
  }
</style>
</head>
<body>
  <div class="banner">
    <div class="book-left" role="img" aria-label="Training book cover for The Craft of a Steady Captain, with a photo of a speaker and audience"></div>

    <div class="headline">
      <h1 class="program-type">Training program</h1>
      <span class="program-rule"></span>
      <p class="program-title">“The Craft of a Steady Captain”</p>
    </div>

    <div class="book-right" role="img" aria-label="Book The Craft of a Steady Captain by Wilfred E. Ashcombe, photo of a seated workshop"></div>
  </div>
</body>
</html>
```